Retail Jewelry Business Card Design Project

We are in need of a new business card design for a retail jewelry store. This store is in the business of fine jewelry including but not specific to bridal jewelry, diamonds, designer jewelry and watches.

This store has been in business for 20 years but continues to strive for a modern professional appeal. The main colors use for this business are a royal blue, white and silver.

Target Market(s)

Target market is ages 18-50

Industry/Entity Type

Jewelry

Requirements
Must have
• Sales Person Name
Sales Person Email Address

Store Address
Store Phone
Website

Standard business card size. No odd shapes or sizes.
Nice to have
• Overall modern feel for card.

We have thought that a design with a nice feature of the logo on the back of the card would be nice but open to ideas.
Should not have
• No specific images of jewelry should be used.

```html
<!DOCTYPE html>
<html lang="en">
<head>
<meta charset="utf-8">
<title>Elliot Marsh Fine Jewelry – Business Cards</title>
<link href="https://fonts.googleapis.com/css2?family=Cinzel:wght@400;600&display=swap" rel="stylesheet">
<style>
  :root {
    --backdrop: #2a1610;
    --royal: #2e2f8f;
    --royal-deep: #2a2b86;
    --royal-light: #3b3f9f;
    --rule-violet: #7b70c4;
    --paper: #ffffff;
    --paper-shade: #eeeeee;
    --white: #ffffff;
  }
  html, body {
    margin: 0;
    padding: 0;
    width: 1200px;
    height: 1000px;
    overflow: hidden;
    background: var(--backdrop);
    font-family: "Cinzel", serif;
  }
  .canvas {
    position: relative;
    width: 1200px;
    height: 1000px;
  }
  .card {
    position: absolute;
    width: 615px;
    height: 360px;
    box-shadow: 0 8px 22px rgba(0,0,0,0.55);
    text-align: center;
  }
  .card--front {
    left: 95px;
    top: 75px;
    background: linear-gradient(160deg, var(--paper) 45%, var(--paper-shade) 100%);
    color: var(--royal);
  }
  .card--back {
    left: 495px;
    top: 545px;
    background: linear-gradient(170deg, var(--royal-light) 0%, var(--royal-deep) 45%, var(--royal) 100%);
    color: var(--white);
  }
  .brand {
    position: absolute;
    left: 0;
    right: 0;
    font-weight: 600;
    letter-spacing: 1px;
  }
  .brand__name {
    display: block;
    font-size: 36px;
    line-height: 1;
  }
  .brand__tag {
    display: block;
    font-size: 17px;
    letter-spacing: 2px;
    margin-top: 18px;
  }
  .card--front .brand { top: 62px; }
  .card--back .brand { top: 62px; }
  .rule {
    position: absolute;
    left: 0;
    width: 100%;
    height: 3px;
    top: 108px;
  }
  .card--front .rule { background: var(--rule-violet); }
  .card--back .rule { background: var(--white); }
  .contact__name {
    position: absolute;
    top: 170px;
    left: 0; right: 0;
    font-size: 21px;
  }
  .contact__email {
    position: absolute;
    top: 203px;
    left: 0; right: 0;
    font-size: 13px;
  }
  .store {
    position: absolute;
    top: 283px;
    left: 0; right: 0;
    font-size: 14px;
    line-height: 22px;
  }
  .website {
    position: absolute;
    top: 255px;
    left: 0; right: 0;
    font-size: 23px;
    letter-spacing: 1px;
  }
</style>
</head>
<body>
<main class="canvas">
  <section class="card card--front" aria-label="Business card front">
    <div class="brand">
      <span class="brand__name">Elliot Marsh</span>
      <span class="brand__tag">FINE JEWELRY</span>
    </div>
    <div class="rule"></div>
    <p class="contact__name" style="margin:0">Elliot Marsh Carrow</p>
    <p class="contact__email" style="margin:0">elliot@marshfinejewelry.com</p>
    <p class="store" style="margin:0">Elliot Marsh Fine<br>2210 Linden Avenue, Harbor City, FL 32000</p>
  </section>

  <section class="card card--back" aria-label="Business card back">
    <div class="brand">
      <span class="brand__name">Elliot Marsh</span>
      <span class="brand__tag">FINE JEWELRY</span>
    </div>
    <div class="rule"></div>
    <p class="website" style="margin:0">www.marshfinejewelry.com</p>
  </section>
</main>
</body>
</html>
```